business card for training & coaching company, Brightwell.co

Create a warm, clean, professional 2-sided business card for Brightwell.co.
Brightwell.co is a new company that shares Brightwell Dialogue (combination of mindfulness, kindness, and nonviolent communication), training and coaching individuals and groups.
Include the logo provided, perhaps incorporating a second opaque version of it as well.
Feelings & Needs lists on the reverse side of the card.

Target Market(s)

Women 30-60 years old, university educated.
Spiritual, may be Buddhist.

Industry/Entity Type

Training

Contact Information for Business Card

Marisabel T. Oberholt, MSc
Group Facilitator & Certified Wellness Coach
Brightwell Dialogue training & support
Group Facilitator & Coach
01632 960 418
07700 900 862
www.brightwell-example.co

Font styles to use
Sans Serif

Requirements
Must have
• Front -- Contact details, logo provided.
• Back -- Feelings list; Needs list
• Professional yet warm, inviting, friendly feel.
Nice to have
• little graphics (telephone for phone number, envelope for email, globe for web);
• Clean font (like Sathu, Frutiga, Helvetica).
• Feeling of movement or transformation.
Should not have
• More than 3 colours.
• Loud or busy designs.
• A gentle curve or two is ok, but not swirly designs.
• No black or other heavy backgrounds.

```html
<!DOCTYPE html>
<html lang="en">
<head>
<meta charset="utf-8">
<title>Brightwell.co business card</title>
<link rel="stylesheet" href="https://fonts.googleapis.com/css2?family=Arimo:wght@400;700&display=swap">
<style>
  :root {
    --orange: #f7941d;
    --orange-deep: #f05a22;
    --red-orange: #ef5a29;
    --peach: #fbd7c1;
    --ink: #333333;
    --white: #ffffff;
    --backdrop: #ecebea;
  }
  * { margin: 0; padding: 0; box-sizing: border-box; }
  html, body {
    width: 1200px; height: 1008px; overflow: hidden;
    background: var(--backdrop);
    font-family: "Arimo", Helvetica, Arial, sans-serif;
  }
  .stage { position: relative; width: 1200px; height: 1008px; }
  .card {
    position: absolute; width: 662px; height: 376px; overflow: hidden;
    box-shadow: 0 8px 22px rgba(0,0,0,0.18);
  }
  .card-front {
    left: 165px; top: 95px;
    background: radial-gradient(ellipse 70% 80% at 50% 35%, var(--white) 45%, var(--peach) 100%);
  }
  .card-back { left: 430px; top: 536px; width: 660px; background: var(--white); }
  .card-shapes { position: absolute; inset: 0; }

  .brand {
    position: absolute; top: 62px; left: 0; right: 0;
    display: flex; justify-content: center; align-items: center; gap: 12px;
    color: var(--orange-deep); font-weight: 700; font-size: 34px;
  }
  .brand-dot { width: 22px; height: 22px; border-radius: 50%; background: var(--orange); }

  .holder-name {
    position: absolute; top: 200px; left: 0; right: 0; text-align: center;
    color: var(--white); font-size: 27px;
  }
  .holder-title {
    position: absolute; top: 236px; left: 0; right: 0; text-align: center;
    color: var(--white); font-size: 18.5px;
  }
  .phones {
    position: absolute; top: 305px; left: 0; right: 0; text-align: center;
    color: var(--red-orange); font-size: 23px;
  }
  .website {
    position: absolute; top: 336px; left: 0; right: 0; text-align: center;
    color: var(--red-orange); font-size: 18px; font-weight: 700; letter-spacing: 9px;
  }

  .list-group { position: absolute; top: 108px; width: 250px; }
  .list-feelings { left: 52px; }
  .list-needs { left: 362px; }
  .list-heading {
    color: var(--red-orange); font-size: 24px; font-weight: 400;
    padding-bottom: 8px; border-bottom: 1px dashed #9a9a9a;
  }
  .list-columns { display: flex; margin-top: 10px; }
  .word-list { list-style: none; font-size: 18px; color: var(--ink); line-height: 22px; }
  .word-list li { padding-left: 14px; position: relative; }
  .word-list li::before {
    content: ""; position: absolute; left: 1px; top: 8px;
    width: 6px; height: 6px; border-radius: 50%; background: var(--red-orange);
  }
  .word-list li.more::before { display: none; }
  .list-feelings .word-list:first-child { width: 135px; }
  .list-needs .word-list:first-child { width: 163px; }
</style>
</head>
<body>
<main class="stage">

  <section class="card card-front" aria-label="Card front">
    <svg class="card-shapes" viewBox="0 0 662 376" preserveAspectRatio="none" aria-hidden="true">
      <defs>
        <linearGradient id="band-fill" x1="0" y1="0" x2="1" y2="1">
          <stop offset="0" stop-color="#f7941d"/>
          <stop offset="1" stop-color="#f05a22"/>
        </linearGradient>
      </defs>
      <path d="M0,135 Q330,225 662,125 L662,318 Q330,255 0,318 Z" fill="url(#band-fill)"/>
    </svg>
    <div class="brand"><span class="brand-dot"></span><span>Brightwell.co</span></div>
    <h1 class="holder-name" style="font-weight:400">Marisabel T. Oberholt</h1>
    <p class="holder-title">MSc &amp; Certified Wellness Coach Group Facilitator &amp; Coach</p>
    <p class="phones">01632 960 418 / 07700 900 862</p>
    <p class="website">www.brightwell-example.co</p>
  </section>

  <section class="card card-back" aria-label="Card back">
    <svg class="card-shapes" viewBox="0 0 660 376" preserveAspectRatio="none" aria-hidden="true">
      <defs>
        <linearGradient id="wave-fill" x1="0" y1="0" x2="1" y2="1">
          <stop offset="0" stop-color="#f7941d"/>
          <stop offset="1" stop-color="#f05a22"/>
        </linearGradient>
      </defs>
      <path d="M0,0 H660 V25 Q330,120 0,35 Z" fill="url(#wave-fill)"/>
      <path d="M0,376 V346 Q330,270 660,350 V376 Z" fill="url(#wave-fill)"/>
    </svg>

    <div class="list-group list-feelings">
      <h2 class="list-heading">FEELINGS</h2>
      <div class="list-columns">
        <ul class="word-list">
          <li>Confusion</li><li>Despair</li><li>Fiery</li><li>Nervous</li><li>Shock</li><li>Weary</li>
        </ul>
        <ul class="word-list">
          <li>Curious</li><li>Edgy</li><li>Grief</li><li>Powerless</li><li>Torn</li><li class="more">&amp; more...</li>
        </ul>
      </div>
    </div>

    <div class="list-group list-needs">
      <h2 class="list-heading">NEEDS</h2>
      <div class="list-columns">
        <ul class="word-list">
          <li>Belonging</li><li>Clarity</li><li>Freedom</li><li>Mourning</li><li>Safety</li><li>Understanding</li>
        </ul>
        <ul class="word-list">
          <li>Choice</li><li>Empathy</li><li>Meaning</li><li>Peace</li><li>Support</li><li class="more">&amp; more...</li>
        </ul>
      </div>
    </div>
  </section>

</main>
</body>
</html>
```